Namecard design for Forex trading & training company

We need a design for a financial forex trading company.
Namecard should give customer a professional yet premium feel, able to differentiate from others.
1) most financial companies employs white background, while its clean and professional, it is too mainstream.
2) I am thinking of brown as base colour, however it easily gives the perception of being an Interior Design company
3) Task is to find a design that is able to portray a clean professional feel, at the same time, appear premium and differentiated from others.
*I'll be employing 3D textured print for my company namecard just so as to give it a better finishing.
Please find attached for my logo.
Financial

```html
<!DOCTYPE html>
<html lang="en">
<head>
<meta charset="utf-8">
<title>Veltrane Capital – Business Card</title>
<link href="https://fonts.googleapis.com/css2?family=Open+Sans:wght@400&family=Tinos:wght@400;700&display=swap" rel="stylesheet">
<style>
  :root {
    --backdrop: #efe4cf;
    --card-dark: #2c1114;
    --brand-blue: #3b4aa3;
    --ink-light: #ffffff;
    --wood-light: #9c8668;
    --wood-mid: #83704f;
    --wood-deep: #6d5c41;
  }
  * { margin: 0; padding: 0; box-sizing: border-box; }
  html, body {
    width: 1189px; height: 1200px; overflow: hidden;
    background: var(--backdrop);
  }
  .canvas { position: relative; width: 1189px; height: 1200px; }
  .card {
    position: absolute; left: 171px; width: 856px; height: 487px;
    overflow: hidden;
  }
  .card--front { top: 68px; background: var(--card-dark); }
  .card--back { top: 627px; }

  .brand {
    position: absolute; left: 0; right: 0; text-align: center;
    font-family: "Tinos", "Times New Roman", serif; font-weight: 400;
    color: var(--brand-blue); letter-spacing: 0.42em;
    display: flex; flex-direction: column; align-items: center; gap: 22px;
  }
  .brand__mark { width: 34px; height: 34px; background: var(--brand-blue); }
  .card--front .brand { top: 230px; font-size: 24px; }

  .front-web {
    position: absolute; left: 0; right: 0; top: 408px;
    display: flex; align-items: center; gap: 14px;
  }
  .front-web .rule { flex: 1; height: 2px; background: var(--ink-light); }
  .front-web .url {
    font-family: "Open Sans", Arial, sans-serif; font-size: 21px;
    color: var(--ink-light);
  }

  .wood {
    position: absolute; inset: 0;
    background: linear-gradient(180deg, var(--wood-light) 0%, var(--wood-mid) 45%, var(--wood-light) 75%, var(--wood-deep) 100%);
  }
  .card--back .brand {
    left: 30px; right: auto; width: 400px; top: 270px; font-size: 19px;
    gap: 18px;
  }

  .contact-panel {
    position: absolute; left: 429px; top: 91px; width: 427px; height: 305px;
    background: var(--card-dark); color: var(--ink-light);
  }
  .person__name {
    position: absolute; left: 44px; top: 36px;
    font-family: "Tinos", "Times New Roman", serif; font-weight: 700; font-size: 31px;
  }
  .person__role {
    position: absolute; left: 44px; top: 72px;
    font-family: "Tinos", "Times New Roman", serif; font-size: 20px;
  }
  .panel-rule { position: absolute; left: 44px; right: 0; height: 2px; background: var(--ink-light); }
  .panel-rule--top { top: 123px; }
  .panel-rule--bottom { top: 221px; }
  .contact-line {
    position: absolute; left: 44px; display: flex; align-items: center; gap: 8px;
    font-family: "Open Sans", Arial, sans-serif; font-size: 21px;
  }
  .contact-line--phone { top: 137px; }
  .contact-line--mail { top: 174px; }
  .contact-line--web { top: 235px; }
  .icon { width: 18px; height: 18px; flex: none; }
</style>
</head>
<body>
<main class="canvas">
  <section class="card card--front" aria-label="Card front">
    <div class="brand">
      <span class="brand__mark"></span>
      <span class="brand__name">VELTRANE CAPITAL</span>
    </div>
    <div class="front-web">
      <span class="rule"></span>
      <span class="url">www.veltranecapital.com</span>
      <span class="rule"></span>
    </div>
  </section>

  <section class="card card--back" aria-label="Card back">
    <div class="wood" role="img" aria-label="Light oak wood grain texture"></div>
    <div class="brand">
      <span class="brand__mark"></span>
      <span class="brand__name">VELTRANE CAPITAL</span>
    </div>
    <div class="contact-panel">
      <p class="person__name">Marcus Lim</p>
      <p class="person__role">Pantry Manager</p>
      <span class="panel-rule panel-rule--top"></span>
      <p class="contact-line contact-line--phone">
        <svg class="icon" viewBox="0 0 18 18" aria-hidden="true"><rect x="5" y="1" width="8" height="16" rx="1.5" fill="none" stroke="#fff" stroke-width="1.4"/><rect x="6.5" y="3" width="5" height="5" fill="#fff"/><path d="M7 11h1M10 11h1M7 13h1M10 13h1M7 15h1M10 15h1" stroke="#fff" stroke-width="1.2"/></svg>
        (86) 555 010 234
      </p>
      <p class="contact-line contact-line--mail">
        <svg class="icon" viewBox="0 0 18 18" aria-hidden="true"><rect x="1" y="3.5" width="16" height="11" fill="#fff"/><path d="M1 3.5l8 6 8-6M1 14.5l6-5M17 14.5l-6-5" fill="none" stroke="#2c1114" stroke-width="1.2"/></svg>
        marcus@veltranecapital.com
      </p>
      <span class="panel-rule panel-rule--bottom"></span>
      <p class="contact-line contact-line--web">www.veltranecapital.com</p>
    </div>
  </section>
</main>
</body>
</html>
```